RB Larks Film Festival Poster

Design a poster for our film festival at the Redbrook University. We would like a graphic clean feel (examples attached).

Must have the following text:

18TH ANNUAL LARKS FILM FESTIVAL
MAY 1, 2 & 3 2015
OTTO VRELAND CINEMA
SCHOOL OF SCREEN AND DIGITAL STORYTELLING
REDBROOK UNIVERSITY
www.larksreelweek.example

Size:
8.5 x 10

Adobe Illustrator please.

Target Market(s)

We will print to poster size and will print to magazines.

Industry/Entity Type

Festival

Colors

Designer to choose colors to be used in the design.

```html
<!DOCTYPE html>
<html lang="en">
<head>
<meta charset="utf-8">
<title>RB Larks Film Festival Poster</title>
<link rel="stylesheet" href="https://fonts.googleapis.com/css2?family=Oswald:wght@300;400;500;600&display=swap">
<style>
  :root {
    --paper: #ffffff;
    --ink: #1b1b1d;
    --plum: #8c3479;
    --sky: #1fa6dd;
    --splash-orange: #f59a1f;
    --splash-pink: #e86aa6;
    --splash-violet: #7a4a9c;
    --splash-red: #d8344f;
  }
  * { margin: 0; padding: 0; box-sizing: border-box; }
  html, body { width: 948px; height: 1200px; overflow: hidden; background: var(--paper); }
  .poster {
    position: relative;
    width: 948px;
    height: 1200px;
    background: var(--paper);
    font-family: "Oswald", "Arial Narrow", sans-serif;
    color: var(--ink);
  }
  .edition {
    position: absolute;
    left: 84px;
    top: 98px;
    font-weight: 300;
    font-size: 58px;
    line-height: 1;
    color: var(--plum);
    letter-spacing: 0.5px;
  }
  .dates {
    position: absolute;
    right: 214px;
    top: 116px;
    font-weight: 300;
    font-size: 40px;
    line-height: 1;
    color: var(--plum);
    letter-spacing: 0.5px;
  }
  .festival-name {
    position: absolute;
    left: 82px;
    top: 158px;
    font-weight: 500;
    font-size: 96px;
    line-height: 1;
    letter-spacing: 1px;
    white-space: nowrap;
  }
  .festival-name .accent { color: var(--sky); }
  .runner-art {
    position: absolute;
    left: 150px;
    top: 300px;
    width: 700px;
    height: 700px;
    border-radius: 46% 54% 40% 60% / 55% 40% 60% 45%;
    background:
      radial-gradient(circle at 30% 35%, var(--splash-orange) 0%, rgba(245,154,31,0) 35%),
      radial-gradient(circle at 60% 30%, var(--splash-violet) 0%, rgba(122,74,156,0) 40%),
      radial-gradient(circle at 45% 60%, var(--splash-pink) 0%, rgba(232,106,166,0) 45%),
      radial-gradient(circle at 35% 85%, var(--splash-red) 0%, rgba(216,52,79,0) 35%),
      radial-gradient(circle at 65% 70%, var(--sky) 0%, rgba(31,166,221,0) 30%);
    opacity: 0.85;
  }
  .venue {
    position: absolute;
    left: 76px;
    top: 1054px;
    font-weight: 400;
    font-size: 46px;
    line-height: 1;
    letter-spacing: 0.5px;
  }
  .venue .accent { color: var(--sky); }
  .host {
    position: absolute;
    left: 78px;
    top: 1112px;
    font-weight: 400;
    font-size: 19px;
    line-height: 1;
    color: var(--plum);
    letter-spacing: 0.2px;
  }
  .website {
    position: absolute;
    left: 78px;
    top: 1142px;
    font-weight: 400;
    font-size: 23px;
    line-height: 1;
    text-transform: uppercase;
    letter-spacing: 0.3px;
  }
</style>
</head>
<body>
  <main class="poster">
    <p class="edition">18TH ANNUAL</p>
    <p class="dates">MAY 1, 2 &amp; 3 2015</p>
    <h1 class="festival-name">LARKS <span class="accent">FILM</span> FESTIVAL</h1>

    <div class="runner-art" role="img" aria-label="Sprinting runner silhouette filled with colourful watercolour paint splashes"></div>

    <p class="venue">OTTO VRELAND <span class="accent">CINEMA</span></p>
    <p class="host">SCHOOL OF SCREEN AND DIGITAL STORYTELLING REDBROOK UNIVERSITY</p>
    <p class="website">www.larksreelweek.example</p>
  </main>
</body>
</html>
```